Bref créative
Business Card, MS Letterhead Template, Envelopes, & E-mail Signature Template for Investment Firm
None - our logo already has the company name included in it
Simple
Peter Dawes
Managing Partner
436 West Fenwick Ave., Suite 210
Charlotte, NC 28202-2731
PDawes@BrambleRidgeLLP.example
www.BrambleRidgeWealthAdvisoryGroup.example
Looking for:
1) Business Cards
2) MS Word Letterhead Template
3) Envelopes - standard size
4) E-mail Signature Template for Outlook
Thanks in advance for your designs and time!
Uploaded the only AI file I have. It has four separate color variations of our logo. We want to use the main logo, which is the blue and gray one. We do not want to use the black and white ones.
This is our logo AI file. Please use the blue and gray one and not the black and white ones.

```html
<!DOCTYPE html>
<html lang="en">
<head>
<meta charset="utf-8">
<title>Email Signature – Peter Dawes</title>
<link rel="stylesheet" href="https://fonts.googleapis.com/css2?family=Cinzel:wght@400;600;700&display=swap">
<style>
  :root {
    --navy: #1f3468;
    --slate: #4d5a74;
    --grey: #8a8f99;
    --rule: #c9ccd2;
    --paper: #ffffff;
  }
  * { margin: 0; padding: 0; box-sizing: border-box; }
  html, body { width: 1200px; height: 871px; overflow: hidden; background: var(--paper); }
  .signature { position: relative; width: 1200px; height: 871px; font-family: "Cinzel", serif; }

  .brand { position: absolute; left: 53px; top: 360px; width: 340px; display: flex; align-items: center; gap: 16px; }
  .brand-square { flex: none; width: 44px; height: 44px; background: var(--navy); }
  .brand-name { color: var(--navy); font-weight: 400; font-size: 20px; line-height: 26px; }

  .divider-v { position: absolute; left: 413px; top: 300px; width: 1.5px; height: 188px; background: var(--rule); }

  .contact { position: absolute; left: 442px; top: 300px; color: var(--grey); }
  .contact-name { font-size: 24px; font-weight: 600; color: var(--slate); letter-spacing: 1px; line-height: 1; }
  .contact-title { font-size: 11px; font-weight: 700; color: var(--navy); letter-spacing: 1.2px; margin-top: 3px; }
  .contact-list { list-style: none; margin-top: 14px; font-size: 13px; line-height: 23px; letter-spacing: 0.4px; }
  .contact-list b { color: var(--navy); font-weight: 700; margin-right: 4px; }
  .contact-web { margin-top: 14px; font-size: 13px; font-weight: 700; color: var(--navy); letter-spacing: 0.6px; }

  .rule-thin { position: absolute; left: 53px; top: 487px; width: 1099px; height: 1.5px; background: var(--rule); }
  .band { position: absolute; left: 53px; top: 521px; width: 1099px; height: 17px; background: var(--navy); }
</style>
</head>
<body>
<div class="signature">
  <div class="brand">
    <div class="brand-square"></div>
    <div class="brand-name">Bramble Ridge<br>Wealth Advisory</div>
  </div>

  <div class="divider-v"></div>

  <div class="contact">
    <div class="contact-name">Peter Dawes</div>
    <div class="contact-title">Managing Partner</div>
    <ul class="contact-list">
      <li>PDawes@BrambleRidgeLLP.example</li>
      <li><b>p.</b>704 555 0140</li>
      <li><b>c.</b>704 555 0162</li>
      <li><b>f.</b>704 555 0141</li>
    </ul>
    <div class="contact-web">www.BrambleRidgeWealthAdvisoryGroup.example</div>
  </div>

  <div class="rule-thin"></div>
  <div class="band"></div>
</div>
</body>
</html>
```